Adult Coloring Book Cover Design

We need a cover created for our New Coloring book.
The title needs to be clear and visible on the front of book. Preferable easy to read when the cover is minimized to about 2 inches on screen. The Full title of the book is:
Morning Meadow Coloring Book: The Gentle Grown-Up Coloring Book for Quiet Hearts Everywhere

This is a Religious Based coloring book. Attached are some images from inside the book, feel free to add them to the cover design. We like color!
Looking for something that is attention grabbing but not too over the top.
front cover is 8.5in width and 11in length. I will need all PSD files in order to make any necessary changes once awarded.

```html
<!DOCTYPE html>
<html lang="en">
<head>
<meta charset="utf-8">
<title>Morning Meadow Coloring Book – Cover</title>
<link rel="stylesheet" href="https://fonts.googleapis.com/css2?family=Fredoka:wght@600&family=Caveat:wght@600&display=swap">
<style>
  :root {
    --page: #e9e6e0;
    --cover: #050505;
    --banner: #ffffff;
    --ink: #111111;
    --red: #e6463a;
    --orange: #f28a24;
    --yellow: #f4c21c;
    --green: #3f9a3a;
    --teal: #1d9bb0;
    --blue: #2f67c8;
    --purple: #6a2fb0;
    --magenta: #c51f8f;
  }
  * { box-sizing: border-box; margin: 0; padding: 0; }
  html, body {
    width: 1161px;
    height: 1200px;
    overflow: hidden;
    background: var(--page);
  }
  .cover {
    position: absolute;
    left: 140px;
    top: 30px;
    width: 880px;
    height: 1140px;
    background: var(--cover);
    overflow: hidden;
  }
  .leaf-wreath {
    position: absolute;
    left: 70px;
    top: 60px;
    width: 740px;
    height: 1010px;
    border-radius: 50%;
    background: conic-gradient(from 0deg,
      var(--blue), var(--purple) 60deg, var(--magenta) 120deg,
      var(--red) 160deg, var(--orange) 200deg, var(--yellow) 240deg,
      var(--green) 280deg, var(--teal) 330deg, var(--blue));
    opacity: 0.92;
  }
  .title-banner {
    position: absolute;
    left: 250px;
    top: 150px;
    width: 380px;
    height: 640px;
  }
  .title-banner svg {
    position: absolute;
    inset: 0;
  }
  .banner-shape {
    fill: var(--banner);
    stroke: var(--ink);
    stroke-width: 10;
    stroke-linejoin: round;
  }
  .title-text {
    position: absolute;
    left: 0;
    right: 0;
    top: 90px;
    text-align: center;
  }
  .title-line {
    display: block;
    font-family: "Fredoka", sans-serif;
    font-weight: 600;
    line-height: 1.02;
    -webkit-background-clip: text;
    background-clip: text;
    color: transparent;
  }
  .line-1 { font-size: 64px; background-image: linear-gradient(90deg, var(--orange), var(--yellow), var(--green)); }
  .line-2 { font-size: 64px; background-image: linear-gradient(90deg, var(--teal), var(--blue)); }
  .line-3 { font-size: 54px; background-image: linear-gradient(90deg, var(--purple), var(--magenta)); }
  .line-4 { font-size: 56px; background-image: linear-gradient(90deg, var(--red), var(--orange)); }
  .subtitle {
    margin: 26px auto 0;
    width: 300px;
    font-family: "Caveat", cursive;
    font-weight: 600;
    font-size: 34px;
    line-height: 1.05;
    color: var(--ink);
  }
</style>
</head>
<body>
  <main class="cover">
    <div class="leaf-wreath" role="img" aria-label="Wreath of striped leaves in rainbow colours surrounding the title"></div>
    <section class="title-banner">
      <svg viewBox="0 0 380 640" width="380" height="640" aria-hidden="true">
        <path class="banner-shape" d="M40 20 Q70 50 100 30 Q190 10 280 30 Q310 50 340 20 L340 70 L360 80 L355 560 L340 570 L350 620 Q300 600 250 610 L190 580 L130 610 Q80 600 30 620 L40 570 L25 560 L20 80 L40 70 Z"/>
      </svg>
      <h1 class="title-text">
        <span class="title-line line-1">MORNING</span>
        <span class="title-line line-2">MEADOW</span>
        <span class="title-line line-3">COLORING</span>
        <span class="title-line line-4">BOOK</span>
        <span class="subtitle" style="display:block">The Gentle Grown-Up Coloring Book for Quiet Hearts Everywhere</span>
      </h1>
    </section>
  </main>
</body>
</html>
```